Quill Harbor Gems Website revamp

Hi,

We need a working WordPress theme, not just a .PSD file. Thank you.

We need a complete revamp of our website. We sell lab grown diamonds online. We sell the idea that everyone should be able to afford a diamond. Thus our diamonds are priced very reasonably. Our selling point "the joy of giving and receiving a diamond in a little box".

Our range of products includes rings, bangles, necklace, ear rings etc. We currently only operate in Singapore. Some photos of our products are on our websites.

Need.
- Clean look and feel, simplistic preferably white and soft colours
- Easy to navigate
- No banners
- E Com
- Introduction page
- Willing to change logo if needed

Existing page: www.quillharborgems-example.com

Target Market(s)

Young ladies
Ladies
Men buying for ladies
Young boyfriends fresh out of school buying for love ones
Working ladies to match what they wear to work

Industry/Entity Type

Online

Requirements
Must have
• ECOM. Product shopping cart
Pictures uploads
Intro page
Nice to have
• Pastel colors preferred. - Color scheme is important in our business to create a long term impression. Color scheme will also be used for next potential project, i.e. packaging design.

Should not have
• Should not have old style fonts.

```html
<!DOCTYPE html>
<html lang="en">
<head>
<meta charset="utf-8">
<title>Quill Harbor Gems</title>
<link href="https://fonts.googleapis.com/css2?family=Roboto+Condensed:wght@400;700&family=Roboto:wght@400;500&display=swap" rel="stylesheet">
<style>
:root{
  --ink:#1f3a48;
  --text:#555b60;
  --muted:#9a9ea2;
  --rule:#e4e4e4;
  --red:#e8141c;
  --soft:#f0f0f0;
  --button:#b9b9b9;
  --icon:#cfd0d2;
}
*{margin:0;padding:0;box-sizing:border-box}
html,body{width:918px;height:1200px;overflow:hidden;background:#fff}
body{position:relative;font-family:"Roboto",Arial,sans-serif;color:var(--text);font-size:9px}
a{color:inherit;text-decoration:none}
ul{list-style:none}
.abs{position:absolute}
h2,h3{font-family:"Roboto Condensed","Arial Narrow",sans-serif;font-weight:400;color:var(--ink);text-transform:uppercase}

/* header */
.brand{left:107px;top:22px;width:120px;font-size:16px;line-height:19px;color:var(--ink);display:flex;gap:6px;align-items:flex-start}
.brand-dot{width:10px;height:10px;border:1px solid var(--ink);margin-top:4px;flex:none}
.search{left:385px;top:22px;width:164px;height:18px;border:1px solid #dcdcdc;padding:0 5px;font-size:8px;color:#b8b8b8;line-height:16px}
.search svg{position:absolute;right:4px;top:3px}
.divider-v{width:1px;height:27px;background:var(--rule);top:16px}
.info{left:580px;top:18px;display:flex;gap:7px}
.info-label{font-size:9px;color:var(--muted)}
.info-value{font-family:"Roboto Condensed",sans-serif;font-size:12px;color:var(--ink)}
.cart-head{left:706px;top:15px;display:flex;gap:7px}
.cart-title{font-family:"Roboto Condensed",sans-serif;font-size:12px;color:var(--ink)}
.cart-sub{font-size:8px;color:var(--muted);margin-top:2px}
.nav{right:108px;top:62px;font-size:9px;color:var(--text)}
.nav span{color:#aaa;margin:0 4px}
.top-rule{left:107px;top:85px;width:703px;height:2px;background:#ececec}

/* sidebar */
.side-rule{left:262px;top:100px;width:1px;height:846px;background:var(--rule)}
.side{left:107px;width:136px}
.side h2{font-size:12px;padding-bottom:7px;border-bottom:1px solid var(--rule)}
.side ul{margin-top:10px}
.side li{height:18.6px;font-size:9px;color:var(--text)}
.side li::before{content:"»";color:#b5b5b5;margin-right:7px;font-size:8px}
.perk{left:107px;width:136px;display:flex;gap:10px;border-top:1px solid var(--rule);padding-top:15px}
.perk h3{font-size:12px}
.perk p{font-size:9px;line-height:12.5px;margin-top:3px}
.cards{display:grid;grid-template-columns:repeat(3,37px);gap:13px 5px;margin-top:8px}
.card{height:23px;border-radius:2px}

/* products */
.section-title{left:279px;font-size:12px}
.grid{left:279px;width:532px;display:flex}
.item{width:139px;height:168px;position:relative}
.item+.item{padding-left:12px}
.item:not(:last-child){border-right:1px solid var(--rule)}
.item:not(:last-child){width:139px}
.item-inner{width:116px;position:relative}
.photo{height:100px;margin:5px auto 0;width:92px;border-radius:40%;background:radial-gradient(circle,#f4f4f5 0%,#d9dadc 60%,#fff 72%)}
.photo.drop{width:70px;border-radius:35%}
.photo.band{height:60px;margin-top:25px;margin-bottom:20px;border-radius:50%}
.sale{position:absolute;right:1px;top:0;background:var(--red);color:#fff;font-size:7px;padding:1px 3px;border-radius:2px;line-height:8px}
.name{text-align:center;font-size:9px;color:var(--text);margin-top:8px;padding-bottom:7px;border-bottom:1px solid var(--rule)}
.price{margin-top:9px;color:var(--red);font-size:11px;line-height:12px}
.was{color:var(--muted);font-size:8px;text-decoration:line-through}
.add{position:absolute;right:0;bottom:-4px;width:30px;height:30px;border-radius:50%;background:var(--soft);display:flex;align-items:center;justify-content:center}
.row-rule{left:279px;width:531px;height:1px;background:var(--rule)}

/* footer */
.foot-rule{left:107px;width:703px;height:1px;background:var(--rule)}
.news{left:107px;top:996px;display:flex;gap:12px}
.news h3{font-size:12px;font-weight:700}
.news p{font-size:9px}
.email{left:389px;top:1002px;width:171px;height:21px;border:1px solid #e2e2e2;font-size:8px;color:#bbb;padding:5px 10px}
.subscribe{left:567px;top:1002px;width:74px;height:21px;background:var(--button);color:#fff;font-family:"Roboto Condensed",sans-serif;font-size:11px;text-align:center;line-height:21px}
.social{left:687px;top:1002px;display:flex;gap:4px}
.social span{width:22px;height:21px;background:var(--icon)}
.col{top:1052px}
.col h3{font-size:12px;margin-bottom:8px}
.col li{font-size:9px;height:17.2px}
.col p{font-size:9px;line-height:13px}
.copy{left:0;width:918px;top:1177px;text-align:center;font-size:9px;color:var(--text)}
</style>
</head>
<body>

<header>
  <div class="abs brand"><span class="brand-dot"></span><span>Quill Harbor Gems</span></div>
  <div class="abs search">Enter Your Keyword...
    <svg width="11" height="11" viewBox="0 0 11 11"><circle cx="4.5" cy="4.5" r="3.5" fill="none" stroke="#bbb" stroke-width="1.2"/><line x1="7" y1="7" x2="10" y2="10" stroke="#bbb" stroke-width="1.3"/></svg>
  </div>
  <div class="abs divider-v" style="left:567px"></div>
  <div class="abs info">
    <svg width="19" height="24" viewBox="0 0 19 24"><rect x="1" y="1" width="7" height="22" rx="1" fill="#cfcfcf"/><rect x="9" y="6" width="9" height="17" rx="1" fill="#dcdcdc"/><g fill="#fff"><rect x="11" y="9" width="2" height="2"/><rect x="14" y="9" width="2" height="2"/><rect x="11" y="13" width="2" height="2"/><rect x="14" y="13" width="2" height="2"/></g></svg>
    <div><div class="info-label">Information Call</div><div class="info-value">+65 9000 4127</div></div>
  </div>
  <div class="abs divider-v" style="left:691px"></div>
  <div class="abs cart-head">
    <svg width="19" height="20" viewBox="0 0 19 20" style="margin-top:5px"><path d="M1 7h17l-2 11H3z" fill="#d3d3d3"/><path d="M5 7l3-5M14 7l-3-5" stroke="#c6c6c6" stroke-width="1.4" fill="none"/></svg>
    <div><div class="cart-title">Shopping Cart</div><div class="cart-sub">0 item(s) &nbsp;| &nbsp;Checkout</div></div>
  </div>
  <nav class="abs nav">Home<span>|</span>Shop<span>|</span>Our Story<span>|</span>Our Diamonds<span>|</span>Customer Login<span>|</span>Create an Account<span>|</span>My Account | Help</nav>
  <div class="abs top-rule"></div>
</header>

<aside>
  <div class="abs side" style="top:100px">
    <h2>Our Product Range</h2>
    <ul><li>Rings</li><li>Bangles</li><li>Necklace</li><li>Ear Rings</li><li>Bracelets</li></ul>
  </div>
  <div class="abs side" style="top:236px">
    <h2>Shop</h2>
    <ul><li>Sort by Newness</li><li>Sort by Popularity</li><li>SOrt by Average Rating</li><li>Sort by Price Low to High</li><li>Sort Price High to Low</li></ul>
  </div>
  <div class="abs perk" style="top:381px">
    <svg width="31" height="39" viewBox="0 0 31 39" style="margin-top:0"><rect x="1" y="1" width="29" height="30" rx="3" fill="#d3d3d3"/><rect x="5" y="5" width="21" height="10" fill="#fff"/><circle cx="7" cy="24" r="2.5" fill="#fff"/><circle cx="24" cy="24" r="2.5" fill="#fff"/><rect x="3" y="31" width="5" height="6" fill="#d3d3d3"/><rect x="23" y="31" width="5" height="6" fill="#d3d3d3"/></svg>
    <div><h3>Free Delivery</h3><p>On All orders over $25<br>Everyday!</p></div>
  </div>
  <div class="abs perk" style="top:455px">
    <svg width="33" height="40" viewBox="0 0 33 40"><circle cx="17" cy="12" r="9" fill="#d3d3d3"/><path d="M1 39c0-11 7-16 16-16s16 5 16 16z" fill="#d3d3d3"/></svg>
    <div><h3>Online Support</h3><p>Email and Live Chat<br>support is available<br>Help link is at the top<br>of the page.</p></div>
  </div>
  <div class="abs side" style="top:554px;border-top:1px solid var(--rule);padding-top:13px">
    <h2 style="border:0;padding:0">Payment Method</h2>
    <div class="cards">
      <span class="card" style="background:#f2e6c8"></span>
      <span class="card" style="background:#eeeeee"></span>
      <span class="card" style="background:#2a6aa8"></span>
      <span class="card" style="background:#c7332a"></span>
      <span class="card" style="background:#1f5296"></span>
    </div>
  </div>
</aside>
<div class="abs side-rule"></div>

<main>
  <h2 class="abs section-title" style="top:100px">New Arrivals</h2>

  <div class="abs grid" style="top:128px">
    <div class="item"><div class="item-inner"><span class="sale">SALE</span><div class="photo" role="img" aria-label="Silver ring with a dark blue stone"></div><div class="name">ETERNITY</div><div class="price">$1,000<div class="was">$1,500</div></div><span class="add"><svg width="12" height="11" viewBox="0 0 12 11"><path d="M0 4h12l-1.5 7h-9z" fill="#777"/><path d="M3 4l2-3M9 4l-2-3" stroke="#777" fill="none"/></svg></span></div></div>
    <div class="item"><div class="item-inner"><div class="photo drop" role="img" aria-label="Diamond drop earrings"></div><div class="name">DROP</div><div class="price">$500<div class="was">$700</div></div><span class="add"><svg width="12" height="11" viewBox="0 0 12 11"><path d="M0 4h12l-1.5 7h-9z" fill="#777"/><path d="M3 4l2-3M9 4l-2-3" stroke="#777" fill="none"/></svg></span></div></div>
    <div class="item"><div class="item-inner"><div class="photo band" role="img" aria-label="Thin diamond bangle"></div><div class="name">BANGS</div><div class="price">$1,000<div class="was">$1,500</div></div><span class="add"><svg width="12" height="11" viewBox="0 0 12 11"><path d="M0 4h12l-1.5 7h-9z" fill="#777"/><path d="M3 4l2-3M9 4l-2-3" stroke="#777" fill="none"/></svg></span></div></div>
    <div class="item"><div class="item-inner"><div class="photo band" role="img" aria-label="Diamond link bracelet"></div><div class="name">PINK</div><div class="price">$1,000<div class="was">$1,500</div></div><span class="add"><svg width="12" height="11" viewBox="0 0 12 11"><path d="M0 4h12l-1.5 7h-9z" fill="#777"/><path d="M3 4l2-3M9 4l-2-3" stroke="#777" fill="none"/></svg></span></div></div>
  </div>
  <div class="abs row-rule" style="top:316px"></div>

  <div class="abs grid" style="top:334px">
    <div class="item"><div class="item-inner"><div class="photo" role="img" aria-label="Silver ring with a dark blue stone"></div><div class="name">ETERNITY</div><div class="price">$1,000<div class="was">$1,500</div></div><span class="add"><svg width="12" height="11" viewBox="0 0 12 11"><path d="M0 4h12l-1.5 7h-9z" fill="#777"/><path d="M3 4l2-3M9 4l-2-3" stroke="#777" fill="none"/></svg></span></div></div>
    <div class="item"><div class="item-inner"><span class="sale">SALE</span><div class="photo drop" role="img" aria-label="Diamond drop earrings"></div><div class="name">DROP</div><div class="price">$500<div class="was">$700</div></div><span class="add"><svg width="12" height="11" viewBox="0 0 12 11"><path d="M0 4h12l-1.5 7h-9z" fill="#777"/><path d="M3 4l2-3M9 4l-2-3" stroke="#777" fill="none"/></svg></span></div></div>
    <div class="item"><div class="item-inner"><span class="sale">SALE</span><div class="photo band" role="img" aria-label="Thin diamond bangle"></div><div class="name">BANGS</div><div class="price">$1,000<div class="was">$1,500</div></div><span class="add"><svg width="12" height="11" viewBox="0 0 12 11"><path d="M0 4h12l-1.5 7h-9z" fill="#777"/><path d="M3 4l2-3M9 4l-2-3" stroke="#777" fill="none"/></svg></span></div></div>
    <div class="item"><div class="item-inner"><div class="photo band" role="img" aria-label="Diamond link bracelet"></div><div class="name">PINK</div><div class="price">$1,000<div class="was">$1,500</div></div><span class="add"><svg width="12" height="11" viewBox="0 0 12 11"><path d="M0 4h12l-1.5 7h-9z" fill="#777"/><path d="M3 4l2-3M9 4l-2-3" stroke="#777" fill="none"/></svg></span></div></div>
  </div>

  <h2 class="abs section-title" style="top:545px">Featured Products</h2>

  <div class="abs grid" style="top:573px">
    <div class="item"><div class="item-inner"><div class="photo" role="img" aria-label="Silver ring with a dark blue stone"></div><div class="name">ETERNITY</div><div class="price">$1,000<div class="was">$1,500</div></div><span class="add"><svg width="12" height="11" viewBox="0 0 12 11"><path d="M0 4h12l-1.5 7h-9z" fill="#777"/><path d="M3 4l2-3M9 4l-2-3" stroke="#777" fill="none"/></svg></span></div></div>
    <div class="item"><div class="item-inner"><div class="photo drop" role="img" aria-label="Diamond drop earrings"></div><div class="name">DROP</div><div class="price">$500<div class="was">$700</div></div><span class="add"><svg width="12" height="11" viewBox="0 0 12 11"><path d="M0 4h12l-1.5 7h-9z" fill="#777"/><path d="M3 4l2-3M9 4l-2-3" stroke="#777" fill="none"/></svg></span></div></div>
    <div class="item"><div class="item-inner"><span class="sale">SALE</span><div class="photo band" role="img" aria-label="Thin diamond bangle"></div><div class="name">BANGS</div><div class="price">$1,000<div class="was">$1,500</div></div><span class="add"><svg width="12" height="11" viewBox="0 0 12 11"><path d="M0 4h12l-1.5 7h-9z" fill="#777"/><path d="M3 4l2-3M9 4l-2-3" stroke="#777" fill="none"/></svg></span></div></div>
    <div class="item"><div class="item-inner"><span class="sale">SALE</span><div class="photo band" role="img" aria-label="Diamond link bracelet"></div><div class="name">PINK</div><div class="price">$1,000<div class="was">$1,500</div></div><span class="add"><svg width="12" height="11" viewBox="0 0 12 11"><path d="M0 4h12l-1.5 7h-9z" fill="#777"/><path d="M3 4l2-3M9 4l-2-3" stroke="#777" fill="none"/></svg></span></div></div>
  </div>
  <div class="abs row-rule" style="top:761px"></div>

  <div class="abs grid" style="top:779px">
    <div class="item"><div class="item-inner"><span class="sale">SALE</span><div class="photo" role="img" aria-label="Silver ring with a dark blue stone"></div><div class="name">ETERNITY</div><div class="price">$1,000<div class="was">$1,500</div></div><span class="add"><svg width="12" height="11" viewBox="0 0 12 11"><path d="M0 4h12l-1.5 7h-9z" fill="#777"/><path d="M3 4l2-3M9 4l-2-3" stroke="#777" fill="none"/></svg></span></div></div>
    <div class="item"><div class="item-inner"><div class="photo drop" role="img" aria-label="Diamond drop earrings"></div><div class="name">DROP</div><div class="price">$500<div class="was">$700</div></div><span class="add"><svg width="12" height="11" viewBox="0 0 12 11"><path d="M0 4h12l-1.5 7h-9z" fill="#777"/><path d="M3 4l2-3M9 4l-2-3" stroke="#777" fill="none"/></svg></span></div></div>
    <div class="item"><div class="item-inner"><div class="photo band" role="img" aria-label="Thin diamond bangle"></div><div class="name">BANGS</div><div class="price">$1,000<div class="was">$1,500</div></div><span class="add"><svg width="12" height="11" viewBox="0 0 12 11"><path d="M0 4h12l-1.5 7h-9z" fill="#777"/><path d="M3 4l2-3M9 4l-2-3" stroke="#777" fill="none"/></svg></span></div></div>
    <div class="item"><div class="item-inner"><div class="photo band" role="img" aria-label="Diamond link bracelet"></div><div class="name">PINK</div><div class="price">$1,000<div class="was">$1,500</div></div><span class="add"><svg width="12" height="11" viewBox="0 0 12 11"><path d="M0 4h12l-1.5 7h-9z" fill="#777"/><path d="M3 4l2-3M9 4l-2-3" stroke="#777" fill="none"/></svg></span></div></div>
  </div>
</main>

<footer>
  <div class="abs foot-rule" style="top:983px"></div>
  <div class="abs news">
    <svg width="26" height="22" viewBox="0 0 26 22" style="margin-top:6px"><path d="M1 11L25 1 19 21 12 15z" fill="#d3d3d3"/><path d="M12 15l13-14" stroke="#fff" stroke-width="1"/></svg>
    <div><h3>Subscribe Our Newsletter!</h3><p>Signup to get exclusive offers from your favorite brands.</p></div>
  </div>
  <div class="abs email">Enter Your Email Address...</div>
  <div class="abs subscribe">SUBSCRIBE</div>
  <div class="abs social"><span></span><span></span><span></span><span></span><span></span></div>
  <div class="abs foot-rule" style="top:1039px"></div>

  <div class="abs col" style="left:107px"><h3>Our Product Range</h3><ul><li>Rings</li><li>Bangles</li><li>Necklace</li><li>Ear Rings</li><li>Bracelets</li></ul></div>
  <div class="abs col" style="left:280px"><h3>Help</h3><ul><li>Contact Us</li><li>About Us</li><li>Shipping</li><li>Help / FAQs</li></ul></div>
  <div class="abs col" style="left:417px"><h3>Company Info</h3><ul><li>Careers</li><li>Terms of Use</li><li>Privacy Policy</li></ul></div>
  <div class="abs col" style="left:556px"><h3>Cart</h3><ul><li>View Cart</li><li>My Account</li><li>Order Status</li><li>Login</li></ul></div>
  <div class="abs col" style="left:695px"><h3>Contact Us</h3><p>27 Lantern Hill Road,<br>#03-12 Harbor Point<br>Centre, Singapore 500126</p><p style="margin-top:13px">Tel: +65 9000 4127</p></div>

  <div class="abs foot-rule" style="top:1168px"></div>
  <p class="abs copy">Copyright © 2013 Quill Harbor Gems. All Rights Reserved.</p>
</footer>

</body>
</html>
```